Linked In Business banner needed

The image size is 1128 px X 191 px

This is a LinkedIn Company Banner. Vantor Quell is the company and I have attached our logo. We are an advance staffing company that only recruits sales professionals.

```html
<!DOCTYPE html>
<html lang="en">
<head>
<meta charset="UTF-8">
<title>Vantor Quell – LinkedIn Company Banner</title>
<link rel="stylesheet" href="https://fonts.googleapis.com/css2?family=Poppins:wght@300;400;600;800&display=swap">
<style>
  :root {
    --navy-deep: #17337a;
    --navy-mid: #24479b;
    --navy-soft: #3a5fb0;
    --sky-accent: #3fbaf6;
    --white: #ffffff;
    --brand-ink: #1d3f8f;
    --tagline-ink: #2a4a92;
  }
  * { margin: 0; padding: 0; box-sizing: border-box; }
  html, body {
    width: 1200px;
    height: 203px;
    overflow: hidden;
    background: var(--navy-deep);
  }
  .banner {
    position: relative;
    width: 1200px;
    height: 203px;
    overflow: hidden;
    font-family: "Poppins", sans-serif;
  }
  .banner__photo {
    position: absolute;
    inset: 0;
    background:
      radial-gradient(ellipse 260px 220px at 330px 190px, rgba(90,125,200,0.45), transparent 70%),
      radial-gradient(ellipse 300px 230px at 680px 120px, rgba(80,115,195,0.4), transparent 70%),
      linear-gradient(90deg, var(--navy-mid) 0%, var(--navy-soft) 30%, var(--navy-mid) 60%, var(--navy-deep) 100%);
  }
  .brand-tab {
    position: absolute;
    top: 0;
    left: 0;
    width: 230px;
    height: 62px;
    background: var(--white);
    border-bottom-right-radius: 32px;
    padding: 13px 0 0 30px;
  }
  .brand-tab__name {
    display: flex;
    align-items: center;
    gap: 6px;
    font-weight: 600;
    font-size: 21px;
    line-height: 1;
    color: var(--brand-ink);
    letter-spacing: -0.2px;
  }
  .brand-tab__dot {
    width: 8px;
    height: 8px;
    background: var(--sky-accent);
  }
  .brand-tab__tagline {
    margin-top: 4px;
    font-weight: 600;
    font-size: 6.5px;
    letter-spacing: 0.4px;
    color: var(--tagline-ink);
    text-transform: uppercase;
    padding-left: 48px;
  }
  .headline {
    position: absolute;
    left: 0;
    right: 0;
    top: 60px;
    text-align: center;
    padding-left: 12px;
  }
  .headline__lead {
    display: block;
    font-weight: 300;
    font-size: 34px;
    line-height: 40px;
    color: var(--white);
    letter-spacing: -0.2px;
  }
  .headline__focus {
    display: block;
    font-weight: 800;
    font-size: 35px;
    line-height: 42px;
    color: var(--sky-accent);
    letter-spacing: 0.2px;
    text-transform: uppercase;
  }
</style>
</head>
<body>
  <header class="banner">
    <div class="banner__photo" role="img" aria-label="Photo of two smiling sales professionals in an office, tinted deep blue"></div>

    <div class="brand-tab">
      <div class="brand-tab__name">Vantor Quell<span class="brand-tab__dot"></span></div>
      <div class="brand-tab__tagline">Your A.I. Sales Recruiter</div>
    </div>

    <h1 class="headline">
      <span class="headline__lead">Advance staffing company that</span>
      <span class="headline__focus">Only recruits sales professionals</span>
    </h1>
  </header>
</body>
</html>
```